Design a Full Page PDF Brochure "white paper" (Adobe InDesign)

Hello, my business needs a template to create "white papers" for our website. These are the free PDF downloads that you see on websites for lead capture.

The winning entry will need the following seven characteristics:
(1) A consistent color palette (or scheme) and feel of our website and logo (which I've attached). Even thought it is called a "white paper", please use lots of color and make it vibrant.
(2) A cover sheet that fills up the whole page, it also needs to have contact information on it (you can use this for now):

Ferris Oakhurst
48 Lindel Rd
Springfield, USA
414-362-8071
ferris@quabbleton.example
[login to view URL]

It's important that our logo is used as part of the cover page design. Feel free to be creative with this.

(3) The text needs to have different sized subheadings (H1, H2, H3)
(4) I would suggest adding "call outs" to highlight quotes from the text
(5) I would suggest submitting entries with multiple page layouts that can be used
(6) You may use Latin text and stock photos that I will replace. Our website [login to view URL] uses a theme of hiking, mountains, and paths.
(7) The final page needs to also have the contact information on it

To help clarify what I'm looking for, here are some examples of white papers:
[login to view URL]
[login to view URL]
[login to view URL]

The entries need to be in Adobe InDesign. The winner needs to turn over the final InDesign Files along with any supporting files such as in Adobe Illustrator.

Also, please do not contact me outside of Taskory (doing so will disqualify your entries).

Thank you ahead of time for your work.

```html
<!DOCTYPE html>
<html lang="en">
<head>
<meta charset="utf-8">
<title>Pathwell White Paper – Cover and Inner Spread</title>
<link rel="stylesheet" href="https://fonts.googleapis.com/css2?family=Montserrat:wght@600;800&family=Open+Sans:wght@400;600&display=swap">
<style>
  :root {
    --backdrop: #4f6a5b;
    --navy: #1e2733;
    --night: #20262e;
    --slate: #5d6b7a;
    --slate-dark: #4a5764;
    --green: #8cc63f;
    --teal: #2fb7c9;
    --paper: #ffffff;
    --ink: #3b4450;
    --callout-bg: #e3f3f8;
    --callout-line: #7ccbe0;
    --sky-top: #5b7fa6;
    --sky-mid: #b9c4cf;
    --hill: #6a6650;
  }
  * { box-sizing: border-box; margin: 0; padding: 0; }
  html, body { width: 1200px; height: 480px; overflow: hidden; }
  body {
    background: var(--backdrop);
    font-family: "Open Sans", Arial, sans-serif;
    color: var(--ink);
    position: relative;
  }
  .spread {
    position: absolute;
    top: 65px;
    width: 540px;
    height: 350px;
    display: flex;
    box-shadow: 0 10px 24px rgba(0,0,0,.35);
  }
  .spread--cover { left: 40px; }
  .spread--inner { left: 620px; }
  .page { position: relative; width: 270px; height: 350px; overflow: hidden; }

  /* Cover spread */
  .cover-photo {
    position: absolute; inset: 0 0 96px 0;
    background: linear-gradient(180deg, var(--sky-top) 0%, var(--sky-mid) 45%, #8a8f93 62%, var(--hill) 82%, #3a3a34 100%);
  }
  .cover-band {
    position: absolute; left: 0; right: 0; bottom: 0; height: 110px;
  }
  .cover-band svg { position: absolute; inset: 0; width: 100%; height: 100%; }
  .logo-box {
    position: absolute; background: var(--navy);
    padding: 7px 10px; display: flex; align-items: center; gap: 5px;
  }
  .logo-box__mark { width: 7px; height: 7px; border-radius: 50%; background: var(--green); }
  .logo-box__name {
    font-family: "Montserrat", Arial, sans-serif; font-weight: 600;
    font-size: 8px; letter-spacing: .08em; color: var(--green); text-transform: uppercase;
  }
  .page--back .logo-box { left: 14px; top: 80px; }
  .page--front .logo-box { right: 14px; top: 12px; }
  .back-copy {
    position: absolute; left: 18px; bottom: 12px; width: 190px; color: #dfe5ea;
  }
  .back-copy__title {
    font-family: "Montserrat", Arial, sans-serif; font-weight: 800; font-size: 9px; color: #fff;
  }
  .back-copy p { font-size: 4.6px; line-height: 1.45; margin-top: 3px; }
  .contact { font-size: 4.6px; line-height: 1.5; margin-top: 4px; }
  .front-copy {
    position: absolute; right: 16px; bottom: 18px; width: 150px; text-align: right;
  }
  .front-copy__kicker {
    font-family: "Montserrat", Arial, sans-serif; font-weight: 600; font-size: 8px;
    color: var(--green); letter-spacing: .05em;
  }
  .front-copy__title {
    font-family: "Montserrat", Arial, sans-serif; font-weight: 800; font-size: 11px; color: var(--teal);
  }
  .front-copy p { font-size: 4.6px; line-height: 1.45; color: #d6dde3; margin-top: 4px; text-align: left; }

  /* Inner spread */
  .page--left, .page--right { background: var(--paper); }
  .page--left { border-right: 1px solid #d7dbe0; }
  .page-header {
    position: absolute; left: 0; right: 0; top: 0; height: 52px;
    background: var(--slate); border-bottom: 2px solid var(--green);
    padding: 12px 16px 0;
  }
  .page-header__kicker {
    font-family: "Montserrat", Arial, sans-serif; font-weight: 600; font-size: 6px;
    letter-spacing: .06em; color: #e8edf1;
  }
  .page-header__title {
    font-family: "Montserrat", Arial, sans-serif; font-weight: 800; font-size: 12px; color: #fff;
  }
  .page-header .logo-box { background: transparent; right: 12px; top: 12px; padding: 0; }
  .page-body { position: absolute; left: 16px; right: 16px; top: 62px; bottom: 40px; }
  .lead { font-size: 5.2px; line-height: 1.45; font-weight: 600; color: var(--slate-dark); margin-bottom: 6px; }
  .cols { display: flex; gap: 10px; }
  .col { flex: 1; }
  .col p { font-size: 4.6px; line-height: 1.5; margin-bottom: 5px; }
  .callout {
    background: var(--callout-bg); border: 1px solid var(--callout-line);
    padding: 8px 7px; margin-bottom: 6px;
  }
  .callout p {
    font-family: "Montserrat", Arial, sans-serif; font-weight: 600;
    font-size: 7px; line-height: 1.4; color: var(--teal); margin: 0;
  }
  .inline-photo {
    width: 100px; height: 86px;
    background: linear-gradient(180deg, #4f86c4 0%, #a9c6df 35%, #e9eef2 48%, #6f8a5a 72%, #3d5a36 100%);
  }
  .caption { font-size: 4.2px; margin-top: 3px; color: var(--slate-dark); }
  .page-footer {
    position: absolute; left: 0; right: 0; bottom: 0; height: 30px;
    background: var(--slate); border-top: 2px solid var(--green);
    padding: 6px 16px; color: #e3e8ec; font-size: 4.2px; line-height: 1.45;
  }
</style>
</head>
<body>

  <section class="spread spread--cover">
    <div class="page page--back">
      <div class="cover-photo" role="img" aria-label="Photo of a winding mountain road under a cloudy sky"></div>
      <div class="cover-band">
        <svg viewBox="0 0 270 110" preserveAspectRatio="none" aria-hidden="true">
          <path d="M0 30 Q140 12 270 2 L270 110 L0 110 Z" fill="#20262e"/>
          <path d="M0 30 Q140 12 270 2" fill="none" stroke="#8cc63f" stroke-width="1.5"/>
        </svg>
      </div>
      <div class="logo-box"><span class="logo-box__mark"></span><span class="logo-box__name">Pathwell</span></div>
      <div class="back-copy">
        <h3 class="back-copy__title">COMPLEX SIMPLE.</h3>
        <p>We guide each client through every choice, from saving and investing to protecting what matters most, so that the path ahead feels simple, steady and truly your own.</p>
        <div class="contact">
          Ferris Oakhurst<br>48 Lindel Rd<br>Springfield, USA<br>414-362-8071<br>ferris@quabbleton.example<br>www.pathwellfinancial.example
        </div>
      </div>
    </div>
    <div class="page page--front">
      <div class="cover-photo" role="img" aria-label="Photo of a winding mountain road continuing into the distance"></div>
      <div class="cover-band">
        <svg viewBox="0 0 270 110" preserveAspectRatio="none" aria-hidden="true">
          <path d="M0 2 Q120 -4 270 24 L270 110 L0 110 Z" fill="#20262e"/>
          <path d="M0 2 Q120 -4 270 24" fill="none" stroke="#8cc63f" stroke-width="1.5"/>
        </svg>
      </div>
      <div class="logo-box"><span class="logo-box__mark"></span><span class="logo-box__name">Pathwell</span></div>
      <div class="front-copy">
        <div class="front-copy__kicker">WE MAKE THE</div>
        <h1 class="front-copy__title">COMPLEX SIMPLE.</h1>
        <p>Planning for the years ahead starts with a clear view of where you stand today and the steps that lead you forward with confidence.</p>
      </div>
    </div>
  </section>

  <section class="spread spread--inner">
    <div class="page page--left">
      <header class="page-header">
        <div class="page-header__kicker">WE MAKE THE</div>
        <h1 class="page-header__title">COMPLEX SIMPLE.</h1>
        <div class="logo-box"><span class="logo-box__mark"></span><span class="logo-box__name">Pathwell</span></div>
      </header>
      <div class="page-body">
        <p class="lead">Planning for the years ahead starts with a clear view of where you stand today and the steps that lead you forward with confidence.</p>
        <div class="cols">
          <div class="col">
            <p>We guide each client through every choice, from saving and investing to protecting what matters most, so that the path ahead feels simple, steady and truly your own.</p>
            <p>We guide each client through every choice, from saving and investing to protecting what matters most, so that the path ahead feels simple, steady and truly your own.</p>
          </div>
          <div class="col">
            <div class="callout"><p>A good plan turns a steep climb into a series of clear, easy steps.</p></div>
            <p>We guide each client through every choice, from saving and investing to protecting what matters most, so that the path ahead feels simple, steady and truly your own.</p>
          </div>
        </div>
      </div>
      <footer class="page-footer">
        Ferris Oakhurst · 48 Lindel Rd, Springfield, USA<br>414-362-8071 · ferris@quabbleton.example<br>www.pathwellfinancial.example
      </footer>
    </div>
    <div class="page page--right">
      <header class="page-header">
        <div class="page-header__kicker">EMOTIONALLY AND INTELLECTUALLY FEEL</div>
        <h2 class="page-header__title">FINANCIAL FREEDOM.</h2>
        <div class="logo-box"><span class="logo-box__mark"></span><span class="logo-box__name">Pathwell</span></div>
      </header>
      <div class="page-body">
        <p class="lead">Planning for the years ahead starts with a clear view of where you stand today and the steps that lead you forward with confidence.</p>
        <div class="cols">
          <div class="col">
            <p>We guide each client through every choice, from saving and investing to protecting what matters most, so that the path ahead feels simple, steady and truly your own.</p>
            <p>We guide each client through every choice, from saving and investing to protecting what matters most, so that the path ahead feels simple, steady and truly your own.</p>
            <p>We guide each client through every choice, from saving and investing to protecting what matters most, so that the path ahead feels simple, steady and truly your own.</p>
          </div>
          <div class="col">
            <div class="inline-photo" role="img" aria-label="Photo of a snow-capped mountain above a green valley"></div>
            <div class="caption">Every summit begins with one step.</div>
          </div>
        </div>
      </div>
      <footer class="page-footer"></footer>
    </div>
  </section>

</body>
</html>
```